依頼詳細
弊社の売りは
・様々な資格を所有したプロが必ず施工する事
・1980年創業 長年の技術と経験
・圧倒的な知識と技術力
・完全自社対応
・静岡県東部エリア限定の地域密着型
・迅速な対応

〇業務内容
害虫駆除サービス
・シロアリ
・スズメバチ
・ゴキブリ
・ノミ、ダニ
・その他

害獣駆除サービス
・ネズミ
・ハクビシン
・コウモリ
・鳥
・その他

ウィルス・除菌・消毒サービス
・除菌、抗菌(光触媒コーティング)
・殺菌、除菌(オゾン処理)
・消臭
・エアコンクリーニング
・その他

住宅環境改善サービス
・害虫.害獣侵入口閉鎖
・床下換気扇取付
・床下湿度改善
・換気口.基礎補修
・その他

記載項目
・はやせ消毒マーク
・会社名:株式会社はやせ消毒
・業務内容:依頼詳細を参考に省略して載せたいです
・役職:代表取締役
・名前(ローマ字):HAYASE KEIJI
・名前(漢字):早瀬 圭二
・本社:〒411-0957静岡県駿東郡長泉町上平原2231-15
・沼津営業所:〒410-0038静岡県沼津市北堀端2754-3
・E-mail:pct.hayase@kujonet-mail.jp
・フリーダイヤル:0120-387-519
・携帯:080-4938-2165

会社のサービス内容が解るイメージ、そして優しさと緊張感が融合してイメージ通りでした。

多くのご提案を頂きありがとうございました。
数少ない情報の中から一生懸命作っていただき感謝しております。
ありがとうございました。

```html
<!DOCTYPE html>
<html lang="ja">
<head>
<meta charset="utf-8">
<title>株式会社はやせ消毒 名刺</title>
<link href="https://fonts.googleapis.com/css2?family=Noto+Sans+JP:wght@400;500;700;900&family=Roboto+Condensed:wght@700&display=swap" rel="stylesheet">
<style>
:root{
  --page:#eeeeee;
  --paper:#ffffff;
  --ink:#222222;
  --brand:#2b5daa;
  --band:#151515;
  --sky:#9db9e2;
  --sky-deep:#6f93c9;
  --gold:#ffd21a;
  --alert:#d9231d;
}
*{margin:0;padding:0;box-sizing:border-box}
html,body{width:831px;height:1200px;overflow:hidden;background:var(--page)}
body{font-family:"Noto Sans JP",sans-serif;color:var(--ink);position:relative}
.card{position:absolute;left:111px;width:610px;height:369px;background:var(--paper);overflow:hidden}
.card--first{top:215px}
.card--second{top:650px}
.abs{position:absolute}
.role{left:30px;top:30px;font-size:11px}
.name{left:28px;top:44px;font-size:31px;font-weight:700;letter-spacing:2px}
.romaji{left:30px;top:88px;font-size:11px;font-weight:700;letter-spacing:1px}
.contact{left:30px;font-size:11px;display:flex;align-items:center;gap:8px}
.contact--mobile{top:122px}
.contact--mail{top:148px}
.ico{width:16px;height:16px;flex:none}
.brand-mark{left:285px;top:22px;width:34px;height:34px;border-radius:50%;background:var(--alert)}
.brand-name{left:328px;top:20px;font-size:21px;font-weight:700;color:var(--brand);letter-spacing:1px}
.brand-sub{left:330px;top:52px;font-size:8px;color:var(--brand);letter-spacing:.5px}
.address{left:300px;top:78px;font-size:10px;line-height:17px}
.band{left:0;top:200px;width:610px;height:34px;background:var(--band);display:flex;align-items:center;padding:0 16px}
.band-lead{color:#fff;font-size:13px;font-weight:700}
.freedial{margin-left:auto;margin-right:70px;display:flex;align-items:center;gap:8px;color:var(--gold);font-family:"Roboto Condensed","Noto Sans JP",sans-serif;font-size:28px;font-weight:700;letter-spacing:1px}
.lower{left:0;top:234px;width:610px;height:135px;background:var(--sky)}
.qual{left:14px;top:12px;width:124px;height:110px;background:#fff;border-radius:6px;padding:10px 9px}
.qual-title{font-size:11px;font-weight:700;color:var(--brand);text-align:center;margin-bottom:8px}
.qual-text{font-size:9px;line-height:15px;color:var(--brand)}
.card--second .qual-title{background:var(--brand);color:#fff;border-radius:3px;padding:2px 0}
.services{left:150px;top:12px;display:flex;gap:22px}
.service{width:90px;display:flex;flex-direction:column;align-items:center;gap:8px}
.service-pic{width:66px;height:66px;border-radius:50%;background:radial-gradient(circle,#ffffff 0%,#dbe6f6 100%);border:2px solid var(--sky-deep)}
.service-label{font-size:10px;font-weight:700;color:#fff;background:var(--sky-deep);border-radius:3px;padding:2px 6px;white-space:nowrap}
.badge-round{left:535px;top:168px;width:58px;height:58px;border-radius:50%;background:var(--alert);color:#fff;font-size:9px;font-weight:700;text-align:center;line-height:13px;padding-top:10px}
.badge-round b{font-size:15px;display:block;line-height:20px}
.badge-box{left:540px;top:150px;width:58px;height:46px;background:var(--gold);color:var(--alert);font-size:9px;font-weight:700;text-align:center;line-height:13px;padding-top:5px;border-radius:3px}
.badge-box b{font-size:15px;display:block;line-height:20px}
</style>
</head>
<body>

<section class="card card--first">
  <p class="abs role">代表取締役</p>
  <h1 class="abs name">早瀬 圭二</h1>
  <p class="abs romaji">HAYASE KEIJI</p>
  <p class="abs contact contact--mobile"><svg class="ico" viewBox="0 0 16 16"><rect x="4" y="1" width="8" height="14" rx="1.5" fill="var(--alert)"/><rect x="5.5" y="3" width="5" height="8" fill="#fff"/></svg>080-4938-2165</p>
  <p class="abs contact contact--mail"><svg class="ico" viewBox="0 0 16 16"><rect x="1" y="3" width="14" height="10" rx="1" fill="var(--alert)"/><path d="M1.5 4 8 9l6.5-5" stroke="#fff" fill="none"/></svg>pct.hayase@kujonet-mail.jp</p>
  <span class="abs brand-mark"></span>
  <p class="abs brand-name">株式会社はやせ消毒</p>
  <p class="abs brand-sub">HAYASE PEST MANAGEMENT PROFESSIONAL</p>
  <p class="abs address">〒411-0957<br>静岡県駿東郡長泉町上平原2231-15<br>[沼津営業所] 〒410-0038<br>静岡県沼津市北堀端2754-3</p>
  <div class="abs band">
    <span class="band-lead">お気軽にご相談ください!</span>
    <span class="freedial"><svg width="30" height="20" viewBox="0 0 30 20"><rect width="30" height="20" rx="4" fill="var(--gold)"/><circle cx="9" cy="10" r="5" fill="var(--band)"/><circle cx="21" cy="10" r="5" fill="var(--band)"/></svg>0120-387-519</span>
  </div>
  <div class="abs badge-round">お見積り<b>無料</b></div>
  <div class="abs lower">
    <div class="abs qual">
      <p class="qual-title">国家資格保有</p>
      <p class="qual-text">害虫駆除から害獣・消毒まで資格を持つプロが一軒一軒丁寧に施工いたします</p>
    </div>
    <div class="abs services">
      <div class="service"><span class="service-pic" role="img" aria-label="害虫駆除のアイコン"></span><span class="service-label">害虫駆除</span></div>
      <div class="service"><span class="service-pic" role="img" aria-label="害獣駆除のアイコン"></span><span class="service-label">害獣駆除</span></div>
      <div class="service"><span class="service-pic" role="img" aria-label="ウィルス・除菌のアイコン"></span><span class="service-label">ウィルス・除菌</span></div>
      <div class="service"><span class="service-pic" role="img" aria-label="住環境改善のアイコン"></span><span class="service-label">住環境改善</span></div>
    </div>
  </div>
</section>

<section class="card card--second">
  <p class="abs role">代表取締役</p>
  <h1 class="abs name">早瀬 圭二</h1>
  <p class="abs romaji">HAYASE KEIJI</p>
  <p class="abs contact contact--mobile"><svg class="ico" viewBox="0 0 16 16"><rect x="4" y="1" width="8" height="14" rx="1.5" fill="var(--alert)"/><rect x="5.5" y="3" width="5" height="8" fill="#fff"/></svg>080-4938-2165</p>
  <p class="abs contact contact--mail"><svg class="ico" viewBox="0 0 16 16"><rect x="1" y="3" width="14" height="10" rx="1" fill="var(--alert)"/><path d="M1.5 4 8 9l6.5-5" stroke="#fff" fill="none"/></svg>pct.hayase@kujonet-mail.jp</p>
  <span class="abs brand-mark"></span>
  <p class="abs brand-name">株式会社はやせ消毒</p>
  <p class="abs brand-sub">HAYASE PEST MANAGEMENT PROFESSIONAL</p>
  <p class="abs address">〒411-0957<br>静岡県駿東郡長泉町上平原2231-15<br>[沼津営業所] 〒410-0038<br>静岡県沼津市北堀端2754-3</p>
  <div class="abs badge-box">出張見積<b>無料</b></div>
  <div class="abs band">
    <span class="band-lead">お気軽にご相談ください!</span>
    <span class="freedial"><svg width="30" height="20" viewBox="0 0 30 20"><rect width="30" height="20" rx="4" fill="var(--gold)"/><circle cx="9" cy="10" r="5" fill="var(--band)"/><circle cx="21" cy="10" r="5" fill="var(--band)"/></svg>0120-387-519</span>
  </div>
  <div class="abs lower">
    <div class="abs qual">
      <p class="qual-title">国家資格保有</p>
      <p class="qual-text">害虫駆除から害獣・消毒まで資格を持つプロが一軒一軒丁寧に施工いたします</p>
    </div>
    <div class="abs services">
      <div class="service"><span class="service-pic" role="img" aria-label="害虫駆除のアイコン"></span><span class="service-label">害虫駆除</span></div>
      <div class="service"><span class="service-pic" role="img" aria-label="害獣駆除のアイコン"></span><span class="service-label">害獣駆除</span></div>
      <div class="service"><span class="service-pic" role="img" aria-label="ウィルス・除菌のアイコン"></span><span class="service-label">ウィルス・除菌</span></div>
      <div class="service"><span class="service-pic" role="img" aria-label="住環境改善のアイコン"></span><span class="service-label">住環境改善</span></div>
    </div>
  </div>
</section>

</body>
</html>
```